Talented Veroka Recruitment company

We require a website for job recruitment company called "Talented Veroka"
Our company is specialising in recruitment of skilled labour from Sri Lanka into Australian market.
We would like to include a job advertising plugin where jobs can be listed and applied for .
COPYWRITING MUST BE INCLUDED !

Industry/Entity Type

Recruitment

Coding

Coded - Design and coding required

Number of Pages Required

5+ page

Colors

Designer to choose colors to be used in the design.

```html
<!DOCTYPE html>
<html lang="en">
<head>
<meta charset="utf-8">
<title>Talented Veroka – Recruitment</title>
<link href="https://fonts.googleapis.com/css2?family=Domine:wght@400;700&family=Montserrat:ital,wght@1,700&family=Open+Sans:ital,wght@0,400;0,600;0,700;1,600;1,700&display=swap" rel="stylesheet">
<style>
:root{
  --blue:#0b4fa8;
  --blue-dark:#083d85;
  --ink:#1b1b1b;
  --grey:#5a5a5a;
  --muted:#8a8a8a;
  --pale:#e6f0fb;
  --slate:#5d6268;
  --white:#ffffff;
}
*{box-sizing:border-box;margin:0;padding:0}
html,body{width:1200px;height:4914px;overflow:hidden;background:var(--white)}
body{position:relative;font-family:"Open Sans",Arial,sans-serif;color:var(--ink)}
.abs{position:absolute}
.serif{font-family:"Domine",Georgia,serif}

/* header */
.brand{left:153px;top:18px;width:200px;font-family:"Domine",Georgia,serif;color:var(--slate);font-weight:700}
.brand .top{font-size:40px;line-height:44px}
.brand .sub{font-size:24px;letter-spacing:11px;color:var(--blue);padding-left:52px;line-height:26px}
.nav{left:528px;top:0;width:672px;height:105px;background:var(--blue);display:flex;gap:44px;padding:64px 0 0 66px}
.nav a{font-family:"Domine",serif;color:var(--white);font-size:13px;text-decoration:none;letter-spacing:.3px}
.nav a.active{text-decoration:underline}

.hero-photo{left:490px;top:105px;width:710px;height:572px;background:linear-gradient(90deg,#f2f3f5 0%,#c9d3e0 30%,#7d95b8 55%,#c4ccd6 80%,#a7b1bd 100%)}
.hero-fade{left:0;top:105px;width:700px;height:572px;background:linear-gradient(90deg,#f4f4f4 60%,rgba(244,244,244,0))}
.hero-bar{left:528px;top:677px;width:672px;height:29px;background:var(--blue)}
.hero-title{left:187px;top:232px;font-size:40px;line-height:50px;font-weight:700;width:380px}
.hero-text{left:187px;top:394px;width:320px;font-size:11px;line-height:14px}
.btn{display:flex;align-items:center;justify-content:center;background:var(--blue);color:var(--white);border-radius:24px;font-family:"Domine",serif;font-size:13px;font-weight:700}
.hero-btn{left:187px;top:443px;width:157px;height:44px}

/* about */
.section-title{font-family:"Domine",serif;font-size:46px;font-weight:700;color:var(--slate);letter-spacing:.5px}
.section-title span{color:var(--blue)}
.about-title{left:151px;top:806px}
.about-lead{left:151px;top:884px;width:380px;font-size:25px;line-height:32px;font-weight:700}
.about-text{left:601px;top:827px;width:450px;font-size:13.5px;line-height:19px;color:#333}
.about-text p+p{margin-top:12px}
.about-photo{left:151px;top:1030px;width:604px;height:338px;background:linear-gradient(120deg,#9aa2ab,#d6d9dc 45%,#5a6169)}
.about-frame{left:654px;top:1097px;width:360px;height:299px;background:var(--white)}
.about-photo2{left:672px;top:1116px;width:341px;height:279px;background:linear-gradient(135deg,#c7b8a4,#8a6c4e 50%,#d7a04a)}

/* how it works */
.how-bg{left:0;top:1700px;width:1200px;height:452px;background:linear-gradient(180deg,#fff 0%,var(--pale) 100%)}
.how-title{left:0;width:1200px;top:1510px;text-align:center}
.how-lead{left:0;width:1200px;top:1593px;text-align:center;font-family:"Domine",serif;font-size:25px;line-height:33px;font-weight:700}
.step-circle{width:190px;height:190px;border-radius:50%;background:#edf3fb;display:flex;align-items:center;justify-content:center}
.step-name{text-align:center;font-family:"Domine",serif;font-size:20px;line-height:27px;font-weight:700}
.step-text{width:240px;text-align:center;font-size:11px;line-height:14.5px;color:#333}

/* split */
.split-left{left:0;top:2152px;width:579px;height:529px;background:linear-gradient(90deg,var(--blue) 55%,#2a5ea4)}
.split-right{left:579px;top:2152px;width:621px;height:529px;background:linear-gradient(90deg,#575c63,#6b6e73 60%,#7a7d80)}
.split-col{width:579px;text-align:center;color:var(--white)}
.split-col h3{font-family:"Domine",serif;font-size:36px;font-weight:700;margin:18px 0 24px}
.split-col p{font-size:14px;line-height:24px;margin:0 auto}
.btn-outline{border:2px solid var(--white);margin:0 auto;width:172px;height:44px}

/* employees */
.emp-title{left:0;width:1200px;top:2752px;text-align:center;font-size:36px}
.emp-card{width:220px;text-align:center}
.avatar{width:164px;height:164px;border-radius:50%;margin:0 auto;background:linear-gradient(180deg,#c9ced4,#56606d)}
.emp-name{margin-top:20px;font-family:"Montserrat","Open Sans",sans-serif;font-size:19px;font-style:italic;font-weight:700;color:var(--blue)}
.emp-text{margin-top:6px;font-size:13px;line-height:17px;color:var(--muted)}
.emp-dot{width:14px;height:14px;border-radius:50%;background:#1976d2;margin:16px auto 0}
.view-btn{left:538px;top:3223px;width:120px;height:42px;font-family:"Open Sans",sans-serif;font-size:12px}

/* postings */
.post-title{left:149px;top:3442px;font-family:"Domine",serif;font-size:37px;line-height:52px;font-weight:700;color:var(--blue)}
.post-card{width:358px;height:280px;background:var(--white);border-radius:22px;box-shadow:0 2px 14px rgba(20,60,120,.12);padding:24px 26px}
.post-card h4{font-size:22px;color:var(--blue);font-weight:700}
.post-card .meta{font-size:13.5px;font-weight:700;color:var(--grey);margin-top:2px}
.post-card .meta small{font-size:10px;margin-left:8px}
.post-card .pay{font-size:12px;font-style:italic;font-weight:600;color:var(--grey);margin-top:16px}
.post-card ul{margin:18px 0 0 16px;font-size:10.5px;line-height:21px;color:var(--grey)}
.post-card li::marker{color:var(--blue)}
.apply{width:150px;height:42px;margin-top:16px;font-family:"Open Sans",sans-serif;font-size:12px}

/* news */
.news-title{left:151px;top:3980px;font-family:"Domine",serif;font-size:48px;color:var(--slate)}
.news-card{width:283px;height:334px;background:var(--white);box-shadow:0 2px 12px rgba(0,0,0,.12)}
.news-img{height:166px}
.news-body{padding:24px 24px 0}
.news-body h5{font-size:13px;line-height:18px;font-weight:700}
.news-body p{font-size:11px;line-height:14px;margin-top:8px}
.news-body .date{display:inline-block;margin-top:10px;font-size:12px;font-weight:700;color:var(--blue);text-decoration:underline}

/* footer */
.footer{left:0;top:4493px;width:1200px;height:421px;background:linear-gradient(180deg,var(--blue) 0%,#0a4aa0 100%);color:var(--white)}
.footer .brand{color:var(--white);left:151px;top:90px}
.footer .brand .sub{color:var(--white)}
.f-contact{left:151px;width:270px;display:flex;align-items:center;gap:16px;font-size:12px;line-height:16px}
.f-icon{width:32px;height:32px;border-radius:50%;background:var(--white);flex:none;display:flex;align-items:center;justify-content:center}
.f-col h6{font-family:"Domine",serif;font-size:28px;font-weight:400;margin-bottom:18px}
.f-col a{display:block;color:var(--white);text-decoration:none;font-size:13px;line-height:30px}
.social{display:flex;align-items:center;gap:14px;font-size:13px;margin-bottom:24px}
.social i{width:34px;height:34px;border:2px solid var(--white);border-radius:50%;display:block}
.copyright{left:0;width:1200px;top:384px;text-align:center;font-family:"Domine",serif;font-size:10px;word-spacing:2px}
.copyright span{margin:0 10px}
</style>
</head>
<body>

<!-- header -->
<div class="abs hero-photo" role="img" aria-label="Smiling recruiter in a blue suit shaking hands across a desk"></div>
<div class="abs hero-fade"></div>
<div class="abs brand"><div class="top">Talented</div><div class="sub">Veroka</div></div>
<nav class="abs nav"><a class="active" href="#">HOME</a><a href="#">ABOUT US</a><a href="#">CAREERS</a><a href="#">AREAS</a><a href="#">CONTACT</a></nav>
<h1 class="abs hero-title serif">A Better Way To Recruit Top Tech Talent</h1>
<p class="abs hero-text">We source skilled, work-ready people from Sri Lanka and place them with trusted Australian employers.</p>
<a class="abs btn hero-btn">LEARN MORE</a>
<div class="abs hero-bar"></div>

<!-- about -->
<h2 class="abs section-title about-title">ABOUT <span>US</span></h2>
<p class="abs about-lead serif">Connecting skilled Sri Lankan talent with Australian employers.</p>
<div class="abs about-text">
  <p>Talented Veroka specialises in recruiting skilled labour from Sri Lanka for the Australian market. We find qualified tradespeople, technicians and professionals who are ready to grow their careers abroad.</p>
  <p>Our team manages screening, skills checks and visa paperwork, so employers meet candidates who are ready to start and workers arrive well prepared for life and work in Australia.</p>
</div>
<div class="abs about-photo" role="img" aria-label="Team of professionals with a smiling woman reaching out to shake hands"></div>
<div class="abs about-frame"></div>
<div class="abs about-photo2" role="img" aria-label="Worker in hard hat and face mask using a tablet on site"></div>

<!-- how it works -->
<div class="abs how-bg"></div>
<h2 class="abs section-title how-title">HOW IT <span>WORKS</span></h2>
<p class="abs how-lead">A clear path from a skilled worker in Sri Lanka<br>to a secure new role in Australia.</p>

<div class="abs step-circle" style="left:153px;top:1721px">
  <svg width="120" height="120" viewBox="0 0 120 120" fill="none" stroke="#0b4fa8" stroke-width="5" stroke-linecap="round">
    <circle cx="70" cy="48" r="32"/><circle cx="70" cy="40" r="9"/><path d="M54 64c4-10 28-10 32 0"/><path d="M47 71 20 98"/><path d="M28 84l8 8"/>
  </svg>
</div>
<svg class="abs" style="left:365px;top:1800px" width="100" height="40" fill="none" stroke="#8a8f96" stroke-width="1.5" stroke-dasharray="3 4"><path d="M2 30C25 4 70 4 92 30"/><circle cx="94" cy="32" r="2" fill="#333"/></svg>
<div class="abs step-circle" style="left:479px;top:1721px">
  <svg width="110" height="120" viewBox="0 0 110 120" fill="none" stroke="#0b4fa8" stroke-width="4" stroke-linecap="round">
    <rect x="25" y="25" width="64" height="80" rx="6"/><path d="M35 18h44"/><circle cx="75" cy="48" r="10"/><path d="M64 66c3-8 19-8 22 0"/><circle cx="36" cy="38" r="12"/><path d="M30 38l5 5 8-9"/><path d="M38 66h18M38 78h38M38 90h38"/>
  </svg>
</div>
<svg class="abs" style="left:705px;top:1800px" width="100" height="40" fill="none" stroke="#8a8f96" stroke-width="1.5" stroke-dasharray="3 4"><path d="M2 10C25 34 70 34 92 10"/><circle cx="94" cy="8" r="2" fill="#333"/></svg>
<div class="abs step-circle" style="left:813px;top:1721px">
  <svg width="120" height="120" viewBox="0 0 120 120" fill="none" stroke="#0b4fa8" stroke-width="5" stroke-linecap="round">
    <circle cx="36" cy="38" r="12"/><path d="M16 74c0-14 9-20 20-20s20 6 20 20"/><circle cx="84" cy="38" r="12"/><path d="M64 74c0-14 9-20 20-20s20 6 20 20"/><path d="M42 96h36"/><path d="M70 88l8 8-8 8"/>
  </svg>
</div>

<p class="abs step-name" style="left:138px;top:1940px;width:220px">Searching for skilled labour from Sri Lanka</p>
<p class="abs step-text" style="left:128px;top:2032px">We reach qualified tradespeople across Sri Lanka through our local network and verify every work history.</p>
<p class="abs step-name" style="left:464px;top:1940px;width:220px">Skillset<br>Required</p>
<p class="abs step-text" style="left:454px;top:2014px">Employers tell us the trade, licences and experience they need. We test each candidate against that skillset before shortlisting.</p>
<p class="abs step-name" style="left:783px;top:1940px;width:250px">We connect these people with employers in Australia.</p>
<p class="abs step-text" style="left:788px;top:2032px">We arrange interviews, prepare visa documents and support each hire until they start work.</p>

<!-- split -->
<div class="abs split-left" role="img" aria-label="Blue-tinted photo of a job seeker in a meeting"></div>
<div class="abs split-right" role="img" aria-label="Grey-tinted photo of employers at a table"></div>
<div class="abs split-col" style="left:27px;top:2250px">
  <svg width="64" height="64" viewBox="0 0 64 64" fill="none" stroke="#fff" stroke-width="3.5" stroke-linecap="round"><rect x="6" y="18" width="46" height="34" rx="4"/><path d="M22 18v-6h14v6M6 30h46"/><circle cx="46" cy="46" r="9" fill="#0b4fa8"/><path d="M53 53l6 6"/></svg>
  <h3>Looking for a Job?</h3>
  <p style="width:380px">Our ability to match the right employee with the right employer has helped many candidates in making life changing move to Australia and to become PERMANENT RESIDENT of Australia.</p>
  <a class="btn btn-outline" style="margin-top:70px">For Employees</a>
</div>
<div class="abs split-col" style="left:596px;top:2250px">
  <svg width="64" height="64" viewBox="0 0 64 64" fill="none" stroke="#fff" stroke-width="3.5"><circle cx="32" cy="20" r="13"/><path d="M10 60c0-14 10-22 22-22s22 8 22 22"/></svg>
  <h3>Looking for Employees?</h3>
  <p style="width:440px">We know, how difficult it is to get the skilled labour force to help with business growth and expansion . That is why we search, screen and select only the best suitable candidates with all documents ready to apply for visa which will dramatically save your time and money.</p>
  <a class="btn btn-outline" style="margin-top:46px">For Employers</a>
</div>

<!-- employees -->
<h2 class="abs section-title emp-title">OUR <span>EMPLOYEES</span></h2>
<svg class="abs" style="left:178px;top:2913px" width="26" height="42" fill="none" stroke="#b8bcc2" stroke-width="3"><path d="M22 2 4 21l18 19"/></svg>
<svg class="abs" style="left:996px;top:2913px" width="26" height="42" fill="none" stroke="#b8bcc2" stroke-width="3"><path d="M4 2l18 19L4 40"/></svg>
<div class="abs emp-card" style="left:220px;top:2851px"><div class="avatar" role="img" aria-label="Portrait of employee"></div><p class="emp-name">Arlo Venn</p><p class="emp-text">Senior consultant placing electricians, welders and builders with firms in Sydney</p><div class="emp-dot"></div></div>
<div class="abs emp-card" style="left:485px;top:2851px"><div class="avatar" role="img" aria-label="Portrait of employee"></div><p class="emp-name">Mira Coldwell</p><p class="emp-text">Visa and migration officer guiding every candidate through documents and approvals</p><div class="emp-dot"></div></div>
<div class="abs emp-card" style="left:749px;top:2851px"><div class="avatar" role="img" aria-label="Portrait of employee"></div><p class="emp-name">Tobin Marsh</p><p class="emp-text">Employer partnerships lead matching Australian businesses with the right skills</p><div class="emp-dot"></div></div>
<a class="abs btn view-btn">VIEW ALL</a>

<!-- postings -->
<svg class="abs" style="left:0;top:3230px" width="1200" height="700" viewBox="0 0 1200 700" preserveAspectRatio="none">
  <defs><linearGradient id="waveFill" x1="0" y1="0" x2="0" y2="1"><stop offset="0" stop-color="#e4eefa"/><stop offset=".6" stop-color="#f3f8fe"/><stop offset="1" stop-color="#ffffff"/></linearGradient></defs>
  <path d="M8 140C120 40 260 70 380 150s330 90 520 30 250-40 300 30V700H8z" fill="url(#waveFill)"/>
</svg>
<h2 class="abs post-title">Employment<br>Postings from JobHarbor</h2>
<div class="abs post-card" style="left:151px;top:3564px">
  <h4>Company Name</h4><p class="meta">Licensed Electrician – Brisbane <small>4.0 ★</small></p>
  <p class="pay">$75,000 - $90,000 a year</p>
  <ul><li>Full-time role on commercial building sites</li><li>Trade certificate and three years' experience needed</li><li>Employer sponsored visa with relocation support</li><li>Overtime and tool allowance included.</li></ul>
  <a class="btn apply">APPLY NOW</a>
</div>
<div class="abs post-card" style="left:538px;top:3564px">
  <h4>Company Name</h4><p class="meta">Structural Welder – Perth <small>4.0 ★</small></p>
  <p class="pay">$72,000 - $85,000 a year</p>
  <ul><li>Fabrication workshop with day shift hours</li><li>MIG and TIG skills with a current trade test</li><li>Employer sponsored visa and airfare covered</li><li>Clear path to permanent residency.</li></ul>
  <a class="btn apply">APPLY NOW</a>
</div>
<svg class="abs" style="left:942px;top:3706px" width="62" height="30" viewBox="0 0 62 30"><circle cx="15" cy="15" r="14" fill="#0b4fa8"/><circle cx="45" cy="15" r="14" fill="#0b4fa8"/><path d="M19 8l-8 7 8 7M41 8l8 7-8 7" fill="none" stroke="#fff" stroke-width="3"/></svg>

<!-- news -->
<h2 class="abs news-title">Latest News</h2>
<div class="abs news-card" style="left:153px;top:4089px"><div class="news-img" role="img" aria-label="Business people shaking hands in an office" style="background:linear-gradient(135deg,#3c4f66,#9fb3c8 60%,#e3e8ee)"></div><div class="news-body"><h5>Australia expands skilled visa list for trades in 2022.</h5><p>Electricians, welders and carpenters see new sponsorship options</p><span class="date">05/11/2022</span></div></div>
<div class="abs news-card" style="left:456px;top:4089px"><div class="news-img" role="img" aria-label="Colleagues greeting each other at a meeting" style="background:linear-gradient(135deg,#e9e6e2,#8a7260 50%,#d6d0c8)"></div><div class="news-body"><h5>Fifty Sri Lankan workers start new roles in Melbourne.</h5><p>Our latest group arrives to join construction and aged care teams</p><span class="date">05/11/2022</span></div></div>
<div class="abs news-card" style="left:759px;top:4089px"><div class="news-img" role="img" aria-label="Interview with a candidate at a laptop" style="background:linear-gradient(135deg,#f1f1f1,#4d4d4d 50%,#b23a3a)"></div><div class="news-body"><h5>Five tips to prepare for your video job interview.</h5><p>Simple steps that help candidates impress Australian employers</p><span class="date">05/11/2022</span></div></div>

<!-- footer -->
<footer class="abs footer">
  <div class="abs brand"><div class="top">Talented</div><div class="sub">Veroka</div></div>
  <div class="abs f-contact" style="top:182px"><span class="f-icon"><svg width="16" height="18" viewBox="0 0 16 18"><path d="M8 1a6 6 0 0 0-6 6c0 5 6 10 6 10s6-5 6-10a6 6 0 0 0-6-6z" fill="#0b4fa8"/><circle cx="8" cy="7" r="2" fill="#fff"/></svg></span>12 Harbour Lane, Colombo 03,<br>Sri Lanka</div>
  <div class="abs f-contact" style="top:228px"><span class="f-icon"><svg width="16" height="16" viewBox="0 0 16 16"><path d="M3 1l3 3-2 2c1 2 3 4 5 5l2-2 3 3-2 3C7 15 1 9 1 3z" fill="#0b4fa8"/></svg></span>555 010 2040</div>
  <div class="abs f-contact" style="top:270px"><span class="f-icon"><svg width="16" height="12" viewBox="0 0 16 12"><rect x="1" y="1" width="14" height="10" rx="1" fill="#0b4fa8"/><path d="M1 2l7 5 7-5" fill="none" stroke="#fff" stroke-width="1.3"/></svg></span>info@talentedveroka.example</div>
  <div class="abs f-col" style="left:469px;top:86px"><h6>Links</h6><a>Home</a><a>About us</a><a>For Employees</a><a>For Employers</a><a>Careers</a><a>Contact</a></div>
  <div class="abs f-col" style="left:664px;top:86px"><h6>Jobs</h6><a>Newspapers</a><a>Social media</a><a>Collecting applications</a></div>
  <div class="abs f-col" style="left:887px;top:86px"><h6>Media</h6>
    <div class="social"><i></i>Circlebook</div><div class="social"><i></i>Chirper</div><div class="social"><i></i>Snapgram</div>
  </div>
  <p class="abs copyright"><span>COPY RIGHTS © 2022 TALENTED VEROKA</span><span>PRIVACY POLICY</span><span>TERMS &amp; CONDITIONS</span></p>
</footer>

</body>
</html>
```